Off Grid consulting and outdoor products needs a website

We need a website design to help launch our new business. Its a business that plans to offer Off-grid conslting and outdoor survival products to people who are looking to relocate or vacation to properties/homes that are Off-grid. We plan to offer design plans for homes/cabins, renewable energy systems for power/heating etc, survival products for outdoor vacations/living. We also do consulting and project management for those who want to design and build from scratch their dream off-grid home or vacation property. I've included our logo design for use.
Would like the website to include 5 pages.
www.bramblequietlands.com
The main landing page (1)
want a video loop backround with a flyover of a cabin in the woods.
https://www.clipvaultmedia.com/video/clip-48213307-pale-sky-thawing-frost-on-pine-slope
(also need a backup static image of just high-shot of cabin in woods)
logo top left, Quoted string of text in the middle, over the video. and a CTA button to 'Contact us'
picture links below that to last 3 recent blog posts.
About Us page (2)
(example) https://larkhollowgear.com/pages/about-lark
Blog page (3)
blog posts associated with pictures.
Consulting 'services' page (4)
-land services and moving off-grid
-Building off grid
-Renewable energy off-grid
-Sustainable farming and all season greenhouses
Store page 'comming soon' (5)
(Example) http://hearthkeep.quillstheme.com/demo-1/demo.html

Target Market(s)

Outdoor enthusiasts and people who want to escape their city life

Coding

Coded - Design and coding required

Requirements
Must have
• Outdoor feel, woods, cabin, reneable energy (solar, geothermal, greenhouses, water wells)

```html
<!DOCTYPE html>
<html lang="en">
<head>
<meta charset="utf-8">
<title>Services – Bramble Quietlands</title>
<link href="https://fonts.googleapis.com/css2?family=Oswald:wght@400;500;600;700&family=Poppins:wght@400;500&display=swap" rel="stylesheet">
<style>
:root{
  --bg:#f0f0f0;
  --bg-clear:rgba(240,240,240,0);
  --ink:#111111;
  --body:#3a3a3a;
  --accent:#5a6b56;
  --line:#b9b9b9;
  --dot:#6b7168;
  --forest-dark:#0c2116;
  --forest-mid:#2f5a44;
  --mist:#d3d8d4;
  --white:#ffffff;
}
*{margin:0;padding:0;box-sizing:border-box}
html,body{width:1200px;height:2770px;overflow:hidden}
body{background:var(--bg);font-family:'Poppins',sans-serif;color:var(--body);position:relative}
.abs{position:absolute;z-index:2}

/* header */
.brand{left:88px;top:40px;display:flex;align-items:center;gap:10px;font-family:'Oswald',sans-serif;font-weight:700;font-size:30px;line-height:1;color:var(--ink);text-transform:uppercase;width:200px}
.brand-mark{width:22px;height:22px;background:var(--ink);flex:none}
.nav{left:606px;top:30px;display:flex;align-items:center;gap:30px;font-family:'Oswald',sans-serif;font-weight:500;font-size:19px;color:var(--ink);text-transform:uppercase}
.nav a{color:inherit;text-decoration:none}
.nav .current{color:var(--accent)}
.menu-toggle{left:1086px;top:34px}

.page-title{left:0;width:1200px;top:148px;text-align:center;font-family:'Oswald',sans-serif;font-weight:700;font-size:66px;color:var(--ink);line-height:1}

/* timeline */
.timeline{left:599px;top:269px;height:1718px;border-left:1px dashed var(--line)}
.timeline-dot{width:9px;height:9px;border-radius:50%;background:var(--dot);left:595px}

.service-photo{width:447px;height:379px}
.service-text{width:456px}
.eyebrow{display:flex;align-items:center;gap:8px;font-family:'Oswald',sans-serif;font-weight:500;font-size:15px;color:var(--accent);text-transform:uppercase}
.eyebrow::before{content:"";width:32px;height:1px;background:var(--accent)}
.service-title{font-family:'Oswald',sans-serif;font-weight:400;font-size:32px;line-height:36px;color:var(--ink);text-transform:uppercase;margin-top:12px;letter-spacing:-.3px}
.service-title.single{white-space:nowrap}
.service-copy{font-size:15px;line-height:26.8px;margin-top:16px;color:var(--body)}

/* forest band */
.forest{position:absolute;z-index:0;left:0;top:1790px;width:1200px;height:980px;
  background:linear-gradient(to bottom,var(--bg-clear) 0%,var(--bg) 8%,var(--mist) 20%,#a9b8ae 32%,var(--forest-mid) 55%,#1b3a29 72%,var(--forest-dark) 86%,#081a10 100%)}

/* footer */
.footer-brand{left:88px;top:2520px;display:flex;align-items:center;gap:10px;font-family:'Oswald',sans-serif;font-weight:700;font-size:34px;line-height:1.05;color:var(--white);text-transform:uppercase;width:210px}
.footer-brand .brand-mark{background:var(--white);width:24px;height:24px}
.footer-col{top:2452px;color:var(--white)}
.footer-col h3{font-family:'Oswald',sans-serif;font-weight:600;font-size:23px;text-transform:uppercase;margin-bottom:10px;letter-spacing:-.2px}
.footer-col li{list-style:none;font-size:14px;line-height:25px}
.contact-line{display:flex;align-items:center;gap:6px;font-size:14px;line-height:25px}
.socials{display:flex;gap:7px;margin-top:14px}
.socials span{width:31px;height:31px;border:1px solid var(--white);border-radius:50%;display:block}
.newsletter p{font-size:14px;line-height:19px;width:250px}
.signup{margin-top:14px;width:250px;height:46px;background:var(--white);display:flex;align-items:center;justify-content:space-between;padding:0 14px 0 19px;color:#333;font-size:16px}
.rule{left:88px;top:2718px;width:1025px;height:1px;background:rgba(255,255,255,.18)}
.copyright{left:0;width:1200px;top:2736px;text-align:center;color:var(--white);font-size:14px}
.to-top{left:1127px;top:2696px;width:40px;height:40px;border-radius:50%;background:rgba(255,255,255,.25);display:flex;align-items:center;justify-content:center}
</style>
</head>
<body>

<div class="forest" role="img" aria-label="Misty evergreen forest seen from above"></div>

<header>
  <div class="abs brand"><span class="brand-mark"></span>Bramble Quietlands</div>
  <nav class="abs nav">
    <svg width="20" height="18" viewBox="0 0 20 18" aria-label="Home"><path d="M10 1 L19 9 H16 V17 H12 V12 H8 V17 H4 V9 H1 Z" fill="#111"/></svg>
    <a href="#">About</a>
    <a href="#" class="current">Services</a>
    <a href="#">Blog</a>
    <a href="#">Store</a>
    <a href="#">Contact Us</a>
  </nav>
  <svg class="abs menu-toggle" width="26" height="18" viewBox="0 0 26 18" aria-label="Menu"><rect x="0" y="0" width="26" height="3" fill="#111"/><rect x="8" y="7" width="18" height="3" fill="#111"/><rect x="4" y="14" width="22" height="3" fill="#111"/></svg>
</header>

<h1 class="abs page-title">SERVICE</h1>

<div class="abs timeline"></div>
<span class="abs timeline-dot" style="top:510px"></span>
<span class="abs timeline-dot" style="top:933px"></span>
<span class="abs timeline-dot" style="top:1357px"></span>
<span class="abs timeline-dot" style="top:1778px"></span>

<!-- service 1 -->
<div class="abs service-photo" style="left:88px;top:305px;background:linear-gradient(160deg,#3b4a2c,#7d8a45 45%,#9a7a4c 70%,#4a3a27)" role="img" aria-label="Canvas tent on a forest path among tall redwoods"></div>
<div class="abs service-text" style="left:664px;top:390px">
  <div class="eyebrow">Services</div>
  <h2 class="service-title single">Land Services and Moving Off-Grid</h2>
  <p class="service-copy">We strive to be aware of the daily details that connect us with the world. We notice sunlight dappling a sidewalk, the taste of a bite of ripe berry, the smell of fall, the feeling of dewy grass on bare feet. These things remind us that we are immersed in nature, no matter.</p>
</div>

<!-- service 2 -->
<div class="abs service-text" style="left:88px;top:813px">
  <div class="eyebrow">Services</div>
  <h2 class="service-title">Building Off Grid</h2>
  <p class="service-copy">We strive to be aware of the daily details that connect us with the world. We notice sunlight dappling a sidewalk, the taste of a bite of ripe berry, the smell of fall, the feeling of dewy grass on bare feet. These things remind us that we are immersed in nature, no matter.</p>
</div>
<div class="abs service-photo" style="left:662px;top:729px;background:linear-gradient(170deg,#8f968f,#4b4f45 40%,#2a2c26 65%,#5a3f24)" role="img" aria-label="Dark A-frame cabin with warm lights in a pine forest"></div>

<!-- service 3 -->
<div class="abs service-photo" style="left:88px;top:1151px;background:linear-gradient(175deg,#9cc6dc,#d9e6ec 18%,#5f6a33 40%,#3f4526 65%,#7fa8c0 85%,#445a3a)" role="img" aria-label="Solar panel rows on a wooded hillside under a blue sky"></div>
<div class="abs service-text" style="left:664px;top:1237px">
  <div class="eyebrow">Services</div>
  <h2 class="service-title">Renewable Energy Off-Grid</h2>
  <p class="service-copy">We strive to be aware of the daily details that connect us with the world. We notice sunlight dappling a sidewalk, the taste of a bite of ripe berry, the smell of fall, the feeling of dewy grass on bare feet. These things remind us that we are immersed in nature, no matter.</p>
</div>

<!-- service 4 -->
<div class="abs service-text" style="left:88px;top:1640px">
  <div class="eyebrow">Services</div>
  <h2 class="service-title">Sustainable Farming and All Season Greenhouses</h2>
  <p class="service-copy">We strive to be aware of the daily details that connect us with the world. We notice sunlight dappling a sidewalk, the taste of a bite of ripe berry, the smell of fall, the feeling of dewy grass on bare feet. These things remind us that we are immersed in nature, no matter.</p>
</div>
<div class="abs service-photo" style="left:662px;top:1573px;background:linear-gradient(180deg,#d8d2c2,#8d8a78 35%,#4f6b32 60%,#2f4a22)" role="img" aria-label="Greenhouse interior with rows of young green crops"></div>

<footer>
  <div class="abs footer-brand"><span class="brand-mark"></span>Bramble Quietlands</div>

  <div class="abs footer-col" style="left:378px">
    <h3>Quick Links</h3>
    <ul><li>About</li><li>Service</li><li>Blog</li><li>Consulting</li><li>Store</li><li>Contact Us</li></ul>
  </div>

  <div class="abs footer-col" style="left:591px">
    <h3>Contact Us</h3>
    <div class="contact-line"><svg width="11" height="14" viewBox="0 0 11 14"><path d="M5.5 0A5.5 5.5 0 0 0 0 5.5C0 9.5 5.5 14 5.5 14S11 9.5 11 5.5A5.5 5.5 0 0 0 5.5 0Zm0 7.5a2 2 0 1 1 0-4 2 2 0 0 1 0 4Z" fill="#9aa59d"/></svg>some goes address here</div>
    <div class="contact-line"><svg width="12" height="12" viewBox="0 0 12 12"><path d="M2.4 0.5 4.3 2.8 3.3 4.3C4 5.9 6.1 8 7.7 8.7L9.2 7.7 11.5 9.6 10.3 11.5C5.5 11.2 .8 6.5.5 1.7Z" fill="#9aa59d"/></svg>+1(123) 555 0142</div>
    <div class="contact-line"><svg width="13" height="10" viewBox="0 0 13 10"><rect width="13" height="10" rx="1" fill="#9aa59d"/><path d="M0.5 1 6.5 5.5 12.5 1" stroke="#1a3a28" fill="none"/></svg>info@bramblequietlands.com</div>
    <div class="socials"><span></span><span></span><span></span><span></span></div>
  </div>

  <div class="abs footer-col newsletter" style="left:862px">
    <h3>Newsletter</h3>
    <p>Be the first to know about new cabins, guides, and promotions.</p>
    <div class="signup">Enter your email
      <svg width="20" height="16" viewBox="0 0 20 16"><rect width="20" height="16" rx="2" fill="#6b6f6c"/><path d="M1 2 10 9 19 2" stroke="#fff" stroke-width="1.6" fill="none"/></svg>
    </div>
  </div>

  <div class="abs rule"></div>
  <p class="abs copyright">©Copyright 2022 Bramblequietlands | All Rights Reserved</p>
  <div class="abs to-top"><svg width="10" height="6" viewBox="0 0 10 6"><path d="M1 5 5 1 9 5" stroke="#fff" stroke-width="1.5" fill="none"/></svg></div>
</footer>

</body>
</html>
```